Morrow Family Reunion Flyer

A flyer detailing family reunion events. It should be complimentary to the logo style and fonts. BE DIFFERENT AVOID TEMPLATES

The 2015 Morrow Family Reunion
Descendants of Tobias Elwin Harold Morrow

Friday August 14th 2pm
Jummah Prayer At Sunvale Mosque
Followed by Family Get Together

Saturday august 15th 12pm
Family Reunion Picnic
4123 morrow Dr.
bowie

Hosted by the Children of The Prestigious Morrow Family

Colors
0355a3
9bcb3c

Requirements
Must have
• Logo

```html
<!DOCTYPE html>
<html lang="en">
<head>
<meta charset="utf-8">
<title>The 2015 Morrow Family Reunion</title>
<link rel="stylesheet" href="https://fonts.googleapis.com/css2?family=Archivo:wght@800;900&family=Fira+Sans:wght@400;700&display=swap">
<style>
  :root {
    --lime: #a2e024;
    --royal: #0b50dc;
    --title-blue: #1652d8;
    --ink: #111111;
    --white: #ffffff;
    --badge-green: #3fae35;
    --badge-ring: #5ec84a;
  }
  * { margin: 0; padding: 0; box-sizing: border-box; }
  html, body { width: 858px; height: 1200px; overflow: hidden; background: var(--lime); }
  .flyer {
    position: relative; width: 858px; height: 1200px; overflow: hidden;
    background: var(--lime); font-family: "Fira Sans", Arial, sans-serif;
  }
  .masthead { position: absolute; left: 0; top: 0; width: 858px; height: 330px; }
  .headline {
    position: absolute; left: 62px; top: 30px;
    font-family: "Archivo", "Arial Black", sans-serif; font-weight: 900;
    color: var(--title-blue); line-height: 1; letter-spacing: -0.5px;
  }
  .headline .year { display: block; font-size: 74px; }
  .headline .surname { display: block; font-size: 104px; margin-top: 8px; letter-spacing: -1px; }
  .headline .event { display: block; font-size: 48px; margin-top: 12px; font-weight: 800; }
  .badge { position: absolute; left: 582px; top: 18px; width: 196px; height: 196px; }
  .badge-name {
    position: absolute; left: 540px; top: 276px; width: 280px; text-align: center;
    font-family: "Fira Sans", Arial, sans-serif; font-weight: 700; font-size: 14px;
    color: var(--badge-green);
  }
  .lineage {
    position: absolute; left: 0; top: 330px; width: 858px; height: 270px;
    background: var(--royal); color: var(--white);
  }
  .lineage-text { position: absolute; left: 88px; top: 18px; line-height: 1; }
  .lineage-text .lead { display: block; font-size: 58px; }
  .lineage-text .given { display: block; font-size: 58px; margin-top: 12px; }
  .lineage-text .ancestor { display: block; font-size: 84px; margin-top: 18px; }
  .ornament-left {
    position: absolute; left: 0; top: 330px; width: 70px; height: 220px;
    background: linear-gradient(160deg, rgba(240,90,200,0.35), rgba(160,230,230,0.25));
  }
  .ornament-right {
    position: absolute; left: 560px; top: 600px; width: 298px; height: 600px;
    background: radial-gradient(ellipse at 70% 40%, rgba(120,200,220,0.45), rgba(250,170,60,0.18) 55%, rgba(0,0,0,0) 80%);
  }
  .schedule { position: absolute; left: 88px; top: 628px; color: var(--ink); font-size: 27px; line-height: 1.36; }
  .schedule .day { font-weight: 700; }
  .schedule .block + .block { margin-top: 40px; }
  .hosts {
    position: absolute; left: 0; top: 965px; width: 858px; height: 235px;
    background: var(--royal); color: var(--white);
  }
  .hosts-intro { position: absolute; left: 88px; top: 30px; font-size: 30px; }
  .hosts-name {
    position: absolute; left: 88px; top: 76px;
    font-family: "Archivo", "Arial Black", sans-serif; font-weight: 800;
    font-size: 30px; line-height: 1.28; letter-spacing: 0.2px;
  }
</style>
</head>
<body>
<main class="flyer">
  <header class="masthead">
    <h1 class="headline">
      <span class="year">THE 2015</span>
      <span class="surname">MORROW</span>
      <span class="event">FAMILY REUNION</span>
    </h1>
    <svg class="badge" viewBox="0 0 196 196" aria-hidden="true">
      <circle cx="98" cy="98" r="92" fill="none" stroke="var(--badge-ring)" stroke-width="6"/>
    </svg>
    <p class="badge-name">Morrow Family Reunion 2015</p>
  </header>

  <section class="lineage">
    <div class="lineage-text">
      <span class="lead">Descendants of</span>
      <span class="given">Tobias Elwin</span>
      <span class="ancestor">Harold Morrow</span>
    </div>
  </section>

  <div class="ornament-left" role="img" aria-label="Colourful floral swirl ornament"></div>
  <div class="ornament-right" role="img" aria-label="Decorative floral tree with curling branches and leaves"></div>

  <section class="schedule">
    <div class="block">
      <p class="day">Friday August 14th 2pm</p>
      <p>Jummah Prayer At Sunvale Mosque</p>
      <p>Followed by Family Get Together</p>
    </div>
    <div class="block">
      <p class="day">Saturday, August 15th, 12pm</p>
      <p>Family Reunion Picnic</p>
      <p>4123 Morrow Dr.</p>
      <p>Bowie</p>
    </div>
  </section>

  <footer class="hosts">
    <p class="hosts-intro">Hosted by</p>
    <p class="hosts-name">THE CHILDREN OF<br>THE PRESTIGIOUS<br>MORROW FAMILY</p>
  </footer>
</main>
</body>
</html>
```